Australia's newest tech recruitment startup

We are a new tech startup in the recruitment space.

We leverage the existing infrastructure of the recruitment network and bundle a value market based business model (like tender loop) that appeals to business.

We are very individual, afraid of no one, minimalist, and defiantly NO "BS"!!

We're not cut price think Varnell Quist rather than Mekari
Updates

Hey Everyone,

thanks so much for your designs. I have eliminated a lot of designs but if I havent to yours then your in with a shot. I would like to see the designs updated with a spot for our twitter handle, my blog address & our linkedIn group address. 

For some designs I think some of the above would look ok on the back of the card so not to make the front look too messy. 

thanks   

Target Market(s)

Our target market is SME's young baby boomer and Gen X

Industry/Entity Type

Business

Requirements
Must have
• Company logo, doesn't have to be both

```html
<!DOCTYPE html>
<html lang="en">
<head>
<meta charset="utf-8">
<title>LinkHire Business Card</title>
<link href="https://fonts.googleapis.com/css2?family=Roboto+Condensed:wght@400;700&display=swap" rel="stylesheet">
<style>
  :root {
    --page-bg: #ffffff;
    --stage-bg: #ededed;
    --brand-blue: #1aa9dd;
    --brand-blue-deep: #2592c0;
    --text-gray: #7a7a7a;
    --text-dark-gray: #6e6e6e;
    --rule-gray: #c9c9c9;
    --band-gray: #8c8c8c;
    --card-white: #ffffff;
    --card-fade: #e3e3e5;
  }
  * { box-sizing: border-box; margin: 0; padding: 0; }
  html, body {
    width: 1200px; height: 902px; overflow: hidden;
    background: var(--page-bg);
    font-family: "Roboto Condensed", Arial, sans-serif;
  }
  .stage {
    position: absolute; left: 184px; top: 148px;
    width: 859px; height: 314px;
    background: var(--stage-bg);
  }
  .card {
    position: absolute; width: 386px; height: 223px;
    border-radius: 14px; overflow: hidden;
    box-shadow: 0 2px 6px rgba(0,0,0,0.18);
  }
  .card-back {
    left: 228px; top: 177px; height: 222px;
    background: radial-gradient(ellipse 70% 80% at 55% 55%, var(--brand-blue) 0%, var(--brand-blue-deep) 100%);
  }
  .brand-name {
    position: absolute; left: 124px; top: 140px;
    font-weight: 700; font-size: 42px; color: #ffffff;
    letter-spacing: 0.5px;
  }
  .card-front {
    left: 635px; top: 176px;
    background: linear-gradient(to bottom, var(--card-fade) 0%, var(--card-white) 45%, var(--card-white) 100%);
  }
  .person { position: absolute; left: 32px; top: 76px; }
  .person-name {
    font-weight: 700; font-size: 23px; color: var(--brand-blue); line-height: 1;
  }
  .person-role {
    margin-top: 5px; font-size: 15px; color: var(--text-dark-gray);
  }
  .divider {
    position: absolute; left: 157px; top: 40px;
    width: 1px; height: 125px;
    background: linear-gradient(to bottom, transparent, var(--rule-gray) 20%, var(--rule-gray) 80%, transparent);
  }
  .contact { position: absolute; left: 188px; top: 57px; list-style: none; }
  .contact li {
    display: flex; align-items: flex-start; gap: 6px;
    font-size: 13px; line-height: 16px; color: var(--text-gray);
    margin-bottom: 8px;
  }
  .contact li:first-child { margin-bottom: 12px; }
  .contact svg { flex: none; margin-top: 1px; }
  .card-band {
    position: absolute; left: 0; bottom: 0;
    width: 386px; height: 32px;
    background: linear-gradient(to right, var(--brand-blue) 0%, var(--brand-blue) 28%, var(--band-gray) 55%, var(--band-gray) 100%);
  }
  .website {
    position: absolute; right: 16px; bottom: 4px;
    font-size: 13px; color: #ffffff; letter-spacing: 0.6px;
  }
</style>
</head>
<body>
  <div class="stage"></div>

  <div class="card card-back">
    <span class="brand-name">LinkHire</span>
  </div>

  <div class="card card-front">
    <div class="person">
      <div class="person-name">Dana Reyes</div>
      <div class="person-role">Director</div>
    </div>
    <div class="divider"></div>
    <ul class="contact">
      <li>
        <svg width="14" height="20" viewBox="0 0 14 20"><path d="M7 0C3.1 0 0 3 0 6.8 0 11.5 7 20 7 20s7-8.5 7-13.2C14 3 10.9 0 7 0z" fill="#1aa9dd"/><circle cx="7" cy="6.8" r="3" fill="#fff"/><circle cx="7" cy="6.8" r="1.5" fill="#1aa9dd"/></svg>
        <span>48 Sample Lane Westfield,<br>Oregon 97001</span>
      </li>
      <li>
        <svg width="16" height="14" viewBox="0 0 16 14"><path d="M1 4C1 1.5 4 0.5 8 0.5S15 1.5 15 4v1.5h-3.5V4h-7v1.5H1z" fill="#1aa9dd"/><path d="M3.5 6h9l1.8 7H1.7z" fill="#1aa9dd"/><circle cx="8" cy="9.3" r="2" fill="#fff"/></svg>
        <span>Phone: (555)010-2468</span>
      </li>
      <li>
        <svg width="16" height="12" viewBox="0 0 16 12"><rect x="0" y="1" width="16" height="11" fill="#1aa9dd"/><path d="M0.5 1.5 8 7.5 15.5 1.5" fill="none" stroke="#fff" stroke-width="1"/></svg>
        <span>dana@LinkHire.com</span>
      </li>
    </ul>
    <div class="card-band" role="img" aria-label="Decorative blue and gray band along the card's bottom edge"></div>
    <span class="website">www.LinkHire.com</span>
  </div>
</body>
</html>
```